Design some Business Cards for new setup company

Please help us to design for name card, letterhead and envelope.

For colour -

Card background: grey
logo: gold
words: red, blue OR orange

Any shade of the above colours are fine, from light to dark, the designer can choose as they wish

Logo design: see attached
Namecard layout: see attached

Corporate identity should include:

a) logo design

b) namecard design

c) letterhead design

d) envelope design

we will want the designer to eventually give us a working file of the image so that we can
1) change names/ do any amendments on our own easily
2) in a format/ program which most people/ printing companies have
3) in a big enough resolution so that the printing will be clear and sharp
4) specifically for letterhead and envelope design, it should also be provided in a format compatible with MS word so that we can use it for our documents

```html
<!DOCTYPE html>
<html lang="en">
<head>
<meta charset="utf-8">
<title>Aldenmere – Business Card</title>
<link rel="stylesheet" href="https://fonts.googleapis.com/css2?family=Source+Sans+3:wght@400;700&display=swap">
<style>
  :root {
    --page: #ffffff;
    --card-light: #ffffff;
    --card-edge: #e3e3e4;
    --card-back: #e8e8e9;
    --panel: #d1d2d4;
    --tab: #d3d4d6;
    --ink: #1a1a1a;
    --brand-gold: #b38a2e;
  }
  * { box-sizing: border-box; margin: 0; padding: 0; }
  html, body {
    width: 1200px; height: 900px; overflow: hidden;
    background: var(--page);
    font-family: "Source Sans 3", "Myriad Pro", Arial, sans-serif;
    color: var(--ink);
  }
  .canvas { position: relative; width: 1200px; height: 900px; }

  .card {
    position: absolute; left: 376px; width: 464px; height: 275px; overflow: hidden;
  }
  .card--front {
    top: 112px;
    background: radial-gradient(ellipse 60% 70% at 50% 40%, var(--card-light) 0%, var(--card-edge) 100%);
  }
  .card--back {
    top: 495px; height: 273px;
    background: radial-gradient(ellipse 70% 80% at 50% 50%, #f1f1f2 0%, var(--card-back) 100%);
  }

  .side-tab {
    position: absolute; top: 28px; width: 47px; height: 217px;
    background: var(--tab);
  }
  .side-tab--left { left: 0; border-radius: 0 10px 10px 0; }
  .side-tab--right { right: 0; border-radius: 10px 0 0 10px; }

  .brand {
    position: absolute; display: flex; align-items: center; gap: 7px;
    color: var(--brand-gold); font-weight: 700; white-space: nowrap;
  }
  .brand__square { background: var(--brand-gold); display: block; }
  .card--front .brand {
    left: 50%; top: 63px; transform: translate(-50%, -50%); font-size: 20px;
  }
  .card--front .brand__square { width: 12px; height: 12px; }

  .contact {
    position: absolute; left: 55px; top: 125px; font-style: normal;
    font-weight: 700; font-size: 16px; line-height: 20px; letter-spacing: -0.2px;
  }
  .person {
    position: absolute; right: 59px; top: 145px; text-align: right;
    font-weight: 400; font-size: 16px; line-height: 20px; letter-spacing: -0.2px;
  }
  .reg-no {
    position: absolute; right: 55px; top: 228px;
    font-weight: 700; font-size: 13px; letter-spacing: -0.1px;
  }

  .back-panel {
    position: absolute; left: 55px; top: 29px; width: 353px; height: 215px;
    background: var(--panel); border-radius: 16px;
  }
  .card--back .brand {
    left: 50%; top: 50%; transform: translate(-50%, -50%); font-size: 34px; gap: 12px;
  }
  .card--back .brand__square { width: 22px; height: 22px; }
</style>
</head>
<body>
<main class="canvas">

  <section class="card card--front" aria-label="Business card front">
    <div class="side-tab side-tab--left"></div>
    <div class="side-tab side-tab--right"></div>

    <div class="brand">
      <span class="brand__square"></span>
      <span class="brand__name">Aldenmere</span>
    </div>

    <address class="contact">
      <div>14 Harbour Lane</div>
      <div>Westfield Park 2041</div>
      <div>+61 2 5550 1837</div>
      <div>hello@aldenmere.com</div>
    </address>

    <div class="person">
      <div>Clara Winthrop</div>
      <div>Managing Director</div>
      <div>B.Com, CPA</div>
    </div>

    <div class="reg-no">Reg. No. 2018457</div>
  </section>

  <section class="card card--back" aria-label="Business card back">
    <div class="back-panel"></div>
    <div class="brand">
      <span class="brand__square"></span>
      <span class="brand__name">Aldenmere</span>
    </div>
  </section>

</main>
</body>
</html>
```